MODERN + COOL Business Card Needed!

SUMMARY
This is for a 40+ year old family business that is transitioning to the 2nd generation and is in real need of a more modern facelift. Ive attached a company logo (I made quickly as an idea with my limited PSD skills) to start off with that you are welcome to change and draw ideas from. Ive also attached some screen shots of cards I like to give you an idea of my preferences.

WHAT WE DO
The company name is Tall Pine HK Ltd. But I prefer to just call it Tall Pine or Tall Pine with Hong Kong as kind of a sub heading on the business card. We own a factory as well as help our customers find factories to make their product. Product I mean, toys 99.9% of the time. Simple old school toys like board games, puzzles, wooden toys, baby/infant toys.

You can say we are a "sourcing" or "trading" or "consulting" company with a factory to help you do it. But since we deal with toys, i like to keep it modern and cool and fun, not serious like managing hedge funds.

WHAT WE ARE LOOKING FOR
A cool, unique looking business card that stands out. In terms of design, something modern and professional. I like darker colored cards and I like colors such as blue/green/dark gray, but am open to other colored themes. I Like bright lime green with gray, always though thats a nice combo. I prefer cards that are all colored and not so much white showing (I think). Ive attached a few screenshots of cards so take a look to get a feel of what I like.

We do alot of wooden stacking games in variety of colors too like Tovra, Lumo, Towerplix (google these to check them out). So designs that sort of resemble stacking or building would be cool but totally not necessary.

In terms of the physical aspects of the card, Im looking for a card a bit different than the standard rectangular shape. Double sided. Little things like having corner(s) be round or different angle instead of square edge I always thought was nice. Its got to be mostly a normal card size, no folding or smaller cards that fit weird in your wallet. No vertical designs. Am open to VERY different/creative shapes (as long as it still fits in a wallet good like a normal buisness card.
Updates

Hi everyone!

Just wanted to write a message to everyone to let them know all submissions are being reviewed or have been reviewed.  If I have not responded with feedback, rest assure your submission was definitely looked at in detail but I either have just been too busy to respond (alot of submissions!), or its on my to be considered list.

I respect and really enjoy receiving everyones creativity and work so I dont want it to go unrecognized - thus this message!  Feel free to submit more ideas if you like until this project ends.  Sometimes some designs just dont click but sometimes they can so you never know!

Thanks again for everyones participation and great work!

~Dev Orr

Target Market(s)

The cards are mainly handed to toy company sourcers and buyers. People I talk to ... say Pelvane for example... might want to make their next edition of Farthingale game with a reputable factory at a good cost so they can sell it to stores at a profit.

So these are the types of people I often try to talk and introduce myself and my company to.

Industry/Entity Type

Building

Colors
acd036
0392cd
00a88e
474747
606060

Requirements
Must have
• Just double sided, not plain rectangle corners, and just cool to look at and catches your eye!

Oh and the obvious business card stuff like place for name, address, number, email, etc.
Nice to have
• Think more modern and fun, not serious and old fashion (thats what we used to be!). Can use the logo I attached and you can definitely alter and change the logo or make a whole new one!

Oh and can definitely use a creative slogan if you like to think of one based on what I described in what we do.
Should not have
• Dont use fonts or text placement that might make "Tall Pine" look like "Tal Lpine"... We arent selling news papers!!

Please nothing related to education since we have the word Pine in the title, thats not our business at all.

Logo and design should not be too heavy on things related to toys, as though thats what we primarily focus on now, what we do may change over time.

```html
<!DOCTYPE html>
<html lang="en">
<head>
<meta charset="utf-8">
<title>Tall Pine Ltd – Business Card</title>
<link rel="stylesheet" href="https://fonts.googleapis.com/css2?family=Open+Sans:ital,wght@0,400;0,600;0,800;1,400&display=swap">
<style>
  :root {
    --backdrop: #e9e6e1;
    --lime-light: #bddd92;
    --lime: #9fcb6b;
    --lime-deep: #8cbf58;
    --band-light: #d4e9bb;
    --white: #ffffff;
    --ink: #2b2b2b;
    --ink-soft: #474747;
    --brand-dark: #1f1f1f;
  }
  * { box-sizing: border-box; margin: 0; padding: 0; }
  html, body {
    width: 1200px; height: 789px; overflow: hidden;
    background: var(--backdrop);
    font-family: "Open Sans", Arial, sans-serif;
  }
  .stage { position: relative; width: 1200px; height: 789px; }

  .card {
    position: absolute; top: 263px;
    width: 454px; height: 294px;
    border-radius: 44px 4px 44px 4px;
    overflow: hidden;
    box-shadow: 0 3px 8px rgba(0,0,0,.28);
  }

  /* Front */
  .card-front {
    left: 140px;
    background: linear-gradient(160deg, var(--lime-light) 0%, var(--lime) 55%, var(--lime-deep) 100%);
  }
  .card-front .bottom-band {
    position: absolute; left: 0; right: 0; bottom: 0; height: 62px;
    background: rgba(255,255,255,.22);
  }
  .card-front .brand {
    position: absolute; left: 96px; top: 160px;
  }

  .brand { display: flex; align-items: flex-start; gap: 10px; }
  .brand-mark {
    width: 30px; height: 30px; background: var(--brand-dark); flex: none; margin-top: 4px;
  }
  .brand-name {
    font-weight: 800; color: var(--brand-dark);
    font-size: 30px; line-height: 1; letter-spacing: -0.5px;
  }
  .brand-sub {
    font-weight: 800; color: var(--brand-dark);
    font-size: 17px; line-height: 1.2; margin-top: 2px;
  }

  /* Back */
  .card-back {
    left: 631px;
    background: var(--white);
  }
  .card-back .bottom-band {
    position: absolute; left: 0; right: 0; bottom: 0; height: 80px;
    background: linear-gradient(180deg, var(--band-light) 0%, var(--lime) 100%);
  }
  .card-back .brand {
    position: absolute; right: 24px; top: 26px; gap: 7px;
  }
  .card-back .brand-mark { width: 22px; height: 22px; margin-top: 2px; }
  .card-back .brand-name { font-size: 22px; }
  .card-back .brand-sub { font-size: 12px; }

  .person { position: absolute; left: 42px; top: 124px; color: var(--ink); }
  .person-name { font-size: 18px; font-weight: 400; line-height: 1.2; }
  .person-role { font-size: 14px; font-style: italic; color: var(--ink-soft); }

  .contacts {
    position: absolute; left: 42px; top: 180px; width: 380px;
    display: grid; grid-template-columns: 188px 1fr; row-gap: 6px;
    font-size: 12px; color: var(--ink);
  }
  .contacts dt { font-weight: 600; display: inline; }
  .contacts dd { display: inline; }
</style>
</head>
<body>
<main class="stage">

  <section class="card card-front" aria-label="Card front">
    <div class="bottom-band"></div>
    <div class="brand">
      <span class="brand-mark"></span>
      <div>
        <div class="brand-name">tall pine ltd</div>
        <div class="brand-sub">hong kong</div>
      </div>
    </div>
  </section>

  <section class="card card-back" aria-label="Card back">
    <div class="bottom-band"></div>
    <div class="brand">
      <span class="brand-mark"></span>
      <div>
        <div class="brand-name">tall pine ltd</div>
        <div class="brand-sub">hong kong</div>
      </div>
    </div>
    <div class="person">
      <div class="person-name">Your Name</div>
      <div class="person-role">Position</div>
    </div>
    <div class="contacts">
      <div><span class="label">Address:</span> xxxxxxxxxxxxxxxx</div>
      <div><span class="label">Email:</span> xxxxxxxxxxxxxxxxxx</div>
      <div><span class="label">Phone:</span> xxxxxxxxxxxxxxxx</div>
      <div><span class="label">Web:</span> xxxxxxxxxxxxxxxx xxx</div>
    </div>
  </section>

</main>
</body>
</html>
```